High Quality Business card for Property Management Agency - Super Classy and professional design

High Quality Business card design.

We need a business card designed for our Property Management Agency.
We are located on Sydney's Northern Beaches and manage beautiful properties along the beach and harbor.
We need a design that oozes modern, classy and professional.
I would like it to be double sided with contact details and logo on the front and just the logo on the back.

I need a print ready PDF version of the file as well as an editable photoshop (PSD) version of the file.

Logo and information details attached.

Target Market(s)

Property owners/investors, Male and Female Aged 28-65

Industry/Entity Type

Real Estate

Contact Information for Business Card

Tom Carrick
Tel: 0467 239 018
Email: tom@harvestlaneestates.com.au
Website: www.harvestlaneestates.com.au
Address: Level 2, 17 Wattlecourt Rd, Dunmarra NSW 2187

Font styles to use
Sans Serif

Requirements
Must have
• - Logo front and back
• - Business card details listed above and attached
• - Colour
Nice to have
• Sleek and professional

```html
<!DOCTYPE html>
<html lang="en">
<head>
<meta charset="utf-8">
<title>Harvest Lane Estates – Business Card</title>
<link href="https://fonts.googleapis.com/css2?family=Montserrat:wght@400;500;600;700&display=swap" rel="stylesheet">
<style>
  :root {
    --page: #e9e8e4;
    --teal: #2bbcc6;
    --teal-deep: #0d7b90;
    --teal-ink: #17788c;
    --ink: #1d1d1d;
    --white: #ffffff;
    --mist: #e6e6e6;
    --sky-top: #d8eef4;
    --sky-low: #9fd0dd;
  }
  * { margin: 0; padding: 0; box-sizing: border-box; }
  html, body { width: 1200px; height: 910px; overflow: hidden; }
  body {
    background: var(--page);
    font-family: "Montserrat", sans-serif;
    position: relative;
  }
  .card {
    position: absolute;
    top: 282px;
    width: 532px;
    height: 315px;
    overflow: hidden;
    box-shadow: 0 10px 18px rgba(0,0,0,0.22);
  }
  .card--front { left: 58px; }
  .card--back { left: 608px; }
  .card__art { position: absolute; inset: 0; }

  .holder-name {
    position: absolute;
    left: 42px;
    top: 96px;
    font-size: 27px;
    font-weight: 700;
    color: var(--teal-ink);
    letter-spacing: 0.2px;
    text-transform: uppercase;
  }
  .contact-list {
    position: absolute;
    left: 42px;
    top: 182px;
    list-style: none;
  }
  .contact-list li {
    display: flex;
    align-items: flex-start;
    gap: 9px;
    font-size: 7.6px;
    font-weight: 500;
    color: var(--teal-ink);
    text-transform: uppercase;
    line-height: 10.5px;
    margin-bottom: 8px;
  }
  .contact-list svg { width: 12px; height: 11px; flex: none; fill: var(--teal-ink); }

  .brand {
    position: absolute;
    font-weight: 600;
    text-transform: uppercase;
    white-space: nowrap;
  }
  .brand--front {
    right: 20px;
    top: 88px;
    font-size: 17px;
    color: var(--ink);
  }
  .brand--back {
    left: 0; right: 0;
    top: 138px;
    text-align: center;
    font-size: 32px;
    color: var(--white);
  }
</style>
</head>
<body>

<section class="card card--front">
  <svg class="card__art" viewBox="0 0 532 315" width="532" height="315">
    <defs>
      <linearGradient id="leftPanel" x1="0" y1="0" x2="1" y2="0">
        <stop offset="0" stop-color="#f4f4f4"/>
        <stop offset="1" stop-color="#dedede"/>
      </linearGradient>
      <linearGradient id="tealBand" x1="0" y1="0" x2="1" y2="0">
        <stop offset="0" stop-color="#1a9aa8"/>
        <stop offset="0.4" stop-color="#3cc3cc"/>
        <stop offset="1" stop-color="#1590a3"/>
      </linearGradient>
      <linearGradient id="skyline" x1="0" y1="0" x2="0" y2="1">
        <stop offset="0" stop-color="#e4f3f7"/>
        <stop offset="0.55" stop-color="#b8dfe8"/>
        <stop offset="0.75" stop-color="#6fb5c6"/>
        <stop offset="1" stop-color="#a9d3de"/>
      </linearGradient>
    </defs>
    <rect width="532" height="315" fill="var(--white)"/>
    <rect y="46" width="532" height="222" fill="url(#leftPanel)"/>
    <polygon points="290,0 532,0 532,46 275,46" fill="url(#tealBand)"/>
    <polygon points="246,46 532,46 532,268 178,268" fill="url(#skyline)"
      role="img" aria-label="Photograph of a waterfront city skyline under a pale sky"/>
    <polygon points="0,268 178,268 0,285" fill="#bfe6ea" opacity="0.8"/>
    <polygon points="258,268 532,268 532,315 242,315" fill="url(#tealBand)"/>
  </svg>

  <h1 class="holder-name">Tom Carrick</h1>
  <ul class="contact-list">
    <li><svg viewBox="0 0 12 11"><path d="M1 4 C1 1 11 1 11 4 L9 5 L8 3.5 L4 3.5 L3 5 Z"/><rect x="2.5" y="6" width="7" height="4.5" rx="1"/></svg>0467 239 018</li>
    <li><svg viewBox="0 0 12 11"><path d="M0.5 2 H11.5 V9.5 H0.5 Z M1.5 3 L6 6.5 L10.5 3 Z" fill-rule="evenodd"/></svg>tom@harvestlaneestates.com.au</li>
    <li><svg viewBox="0 0 12 11"><circle cx="6" cy="5.5" r="5"/><path d="M1 5.5 H11 M6 0.5 V10.5" stroke="#fff" stroke-width="0.8"/></svg>www.harvestlaneestates.com.au</li>
    <li><svg viewBox="0 0 12 11"><path d="M6 0.5 L11.5 5.5 H10 V10.5 H7.2 V7.5 H4.8 V10.5 H2 V5.5 H0.5 Z"/></svg><span>Level 2, 17 Wattlecourt Rd<br>Dunmarra NSW 2187</span></li>
  </ul>

  <div class="brand brand--front">Harvest Lane Estates</div>
</section>

<section class="card card--back">
  <svg class="card__art" viewBox="0 0 532 315" width="532" height="315">
    <defs>
      <linearGradient id="backFill" x1="0" y1="0" x2="1" y2="0.3">
        <stop offset="0" stop-color="#2cbfc8"/>
        <stop offset="0.55" stop-color="#27b3bf"/>
        <stop offset="1" stop-color="#0d7790"/>
      </linearGradient>
    </defs>
    <rect width="532" height="315" fill="url(#backFill)"/>
  </svg>
  <div class="brand brand--back">Harvest Lane Estates</div>
</section>

</body>
</html>
```